We need a refreshed business card. Our company is a venture capital investment firm focused on investing in medical devices. Logo is attached. please also see our website www.velmoracapital.example

Target Market(s)

investors and potential investment targets

Industry/Entity Type

medical investments

Contact Information for Business Card

logo, name, title, email, phone, website, address,

Colors
0054AA
0677BA
7BADD7
CADEEF
E8F1F8
0094D4
00A9DD
6FCCEA
C7EBF8
E9F6FB
00AB8E
00BBA5
67D7C9
C6EFE9
E9F9F6

Requirements
Must have
• fresh modern design
Nice to have
• QR code leading to our linked in page, short description of what we do “Early Stage Medical Device Investors”

```html
<!DOCTYPE html>
<html lang="en">
<head>
<meta charset="utf-8">
<title>Velmora Business Card</title>
<link href="https://fonts.googleapis.com/css2?family=Roboto:wght@400;500;700&family=Lato:wght@400&display=swap" rel="stylesheet">
<style>
  :root {
    --page: #eef0f2;
    --white: #ffffff;
    --navy: #0556a6;
    --teal: #00ab8e;
    --teal-band: #03aa94;
    --ink: #3f4347;
    --icon: #0556a6;
  }
  * { margin: 0; padding: 0; box-sizing: border-box; }
  html, body { width: 1200px; height: 1200px; overflow: hidden; background: var(--page); }
  body { position: relative; font-family: "Roboto", Arial, sans-serif; }

  .card { position: absolute; left: 222px; width: 754px; height: 463px; overflow: hidden; }
  .card--front { top: 105px; background: var(--white); }
  .card--back { top: 630px; background: var(--navy); }

  .brand { position: absolute; display: flex; align-items: center; gap: 12px; font-weight: 500; }
  .brand__dot { border-radius: 50%; background: var(--teal); }
  .card--front .brand { right: 60px; top: 72px; color: var(--navy); font-size: 62px; }
  .card--front .brand__dot { width: 18px; height: 18px; }

  .contact { position: absolute; left: 44px; top: 165px; list-style: none; }
  .contact li { display: flex; align-items: center; gap: 10px; height: 31px; font-size: 21px; color: var(--ink); }
  .contact svg { width: 21px; height: 21px; fill: var(--icon); flex: none; }
  .address { position: absolute; left: 44px; top: 300px; font-size: 21px; color: var(--ink); }

  .front-rule { position: absolute; left: 0; top: 345px; width: 100%; height: 10px; background: var(--teal); }
  .nameplate { position: absolute; left: 0; top: 355px; width: 100%; height: 108px; background: var(--navy); color: var(--white); padding: 22px 0 0 45px; }
  .nameplate__name { font-size: 34px; font-weight: 700; line-height: 1.1; }
  .nameplate__title { font-size: 22px; font-weight: 400; margin-top: 2px; }

  .card--back .brand { left: 0; right: 0; top: 130px; justify-content: center; color: var(--white); font-size: 84px; }
  .card--back .brand__dot { width: 24px; height: 24px; background: var(--white); }
  .back-rule { position: absolute; left: 0; top: 348px; width: 100%; height: 12px; background: var(--white); }
  .back-band { position: absolute; left: 0; top: 360px; width: 100%; height: 103px; background: var(--teal-band); display: flex; align-items: center; justify-content: center; }
  .back-band__url { font-family: "Lato", Arial, sans-serif; font-size: 21px; letter-spacing: 3.5px; color: var(--white); }
</style>
</head>
<body>
  <section class="card card--front">
    <div class="brand"><span class="brand__dot"></span>Velmora</div>
    <ul class="contact">
      <li><svg viewBox="0 0 24 24"><path d="M6.6 10.8c1.4 2.8 3.8 5.1 6.6 6.6l2.2-2.2c.3-.3.7-.4 1-.2 1.1.4 2.3.6 3.6.6.6 0 1 .4 1 1V20c0 .6-.4 1-1 1C10.6 21 3 13.4 3 4c0-.6.4-1 1-1h3.5c.6 0 1 .4 1 1 0 1.3.2 2.5.6 3.6.1.3 0 .7-.2 1L6.6 10.8z"/></svg>415.555.0142</li>
      <li><svg viewBox="0 0 24 24"><path d="M6 2h12v5H6zM4 8h16a2 2 0 0 1 2 2v6h-4v-3H6v3H2v-6a2 2 0 0 1 2-2zm3 6h10v8H7z"/></svg>415.555.0187</li>
      <li><svg viewBox="0 0 24 24"><path d="M2 4h20v10h-2V7l-8 6-8-6v11h10v2H2zm2 0 8 6 8-6zM17 19l2 2 4-4-1.4-1.4L19 18.2l-.6-.6z"/></svg>hello@velmoracapital.example</li>
      <li><svg viewBox="0 0 24 24"><path d="M12 2a10 10 0 1 0 0 20 10 10 0 0 0 0-20zm6.9 6h-2.9a15 15 0 0 0-1.3-3.6A8 8 0 0 1 18.9 8zM12 4c.8 1.2 1.5 2.5 1.9 4h-3.8c.4-1.4 1.1-2.8 1.9-4zM4.3 14a8 8 0 0 1 0-4h3.4a16 16 0 0 0 0 4zm.8 2h2.9c.3 1.3.8 2.5 1.3 3.6A8 8 0 0 1 5.1 16zM8 8H5.1a8 8 0 0 1 4.2-3.6C8.8 5.5 8.3 6.7 8 8zm4 12c-.8-1.2-1.5-2.5-1.9-4h3.8c-.4 1.4-1.1 2.8-1.9 4zm2.3-6H9.7a14 14 0 0 1 0-4h4.6a14 14 0 0 1 0 4zm.4 5.6c.5-1.1 1-2.3 1.3-3.6h2.9a8 8 0 0 1-4.2 3.6zm1.6-5.6a16 16 0 0 0 0-4h3.4a8 8 0 0 1 0 4z"/></svg>www.velmoracapital.example</li>
    </ul>
    <p class="address">Harbor Lane Suite 210 San Francisco, CA 94107</p>
    <div class="front-rule"></div>
    <div class="nameplate">
      <p class="nameplate__name">Marlen Ostrova</p>
      <p class="nameplate__title">Principal Account Executive</p>
    </div>
  </section>

  <section class="card card--back">
    <div class="brand"><span class="brand__dot"></span>Velmora</div>
    <div class="back-rule"></div>
    <div class="back-band"><p class="back-band__url">www.velmoracapital.example</p></div>
  </section>
</body>
</html>
```